Redesign Call Answering Service Company Website

There is a good explanation of what we do at existing website hummingdesk.com.au.

We are getting traffic and now want to increase conversions and reduce drop offs. We need to create trust very quickly.

Once website done we will be looking to redesign logo.

We want to use “F” shaped reading pattern for website viewers. 2 very rough ideas on attached wireframes docs. The winning site only needs to follow the rough layout – no need for boxes, etc. Looking for creative help here!

One page needed (home page) that easily becomes all other pages without a "price reference" (see wire frames).

All existing pages will have new/updated content added with extra pages added.

Target Market(s)

Target market to appeal to is 70% females 25 to 60, self-employed business owners, complimentary/alternative therapists, small to medium business ente

Industry/Entity Type

It Company

Requirements
Must have
• must have items on wire frames
must have a Client Login (to self-service area)
must have a Contact Area with 4 x phone numbers, 1 x fax number and email/contact us

```html
<!DOCTYPE html>
<html lang="en">
<head>
<meta charset="utf-8">
<title>Humming Desk – Phone Answering</title>
<link href="https://fonts.googleapis.com/css2?family=Ubuntu:wght@400;500;700&family=Arimo:wght@400;700&display=swap" rel="stylesheet">
<style>
:root{
  --blue:#1b82c9;
  --blue-dark:#0f6aae;
  --blue-light:#5cb4ea;
  --ink:#333;
  --char:#2b2b2b;
  --white:#fff;
  --line:#d9d9d9;
}
*{box-sizing:border-box;margin:0;padding:0}
html,body{width:1150px;height:1200px;overflow:hidden}
body{background:linear-gradient(90deg,#cfcfcf,#e2e2e2 50%,#cfcfcf);font-family:Arimo,Arial,sans-serif;color:var(--ink);position:relative}
.abs{position:absolute}
.sheet{left:77px;top:0;width:996px;height:1166px;background:var(--white)}
.header{left:77px;top:0;width:996px;height:107px;background:linear-gradient(#fff,#ececec);border-top:3px solid #444}
.brand{left:97px;top:34px;font:700 35px Ubuntu,sans-serif;color:var(--blue)}
.tagline{right:90px;top:50px;text-align:right;font:700 20px Ubuntu,sans-serif;color:var(--blue);line-height:23px}
.tagline span{display:block;color:#666}
.login{left:737px;top:0;width:322px;height:34px;background:var(--char);border-radius:0 0 14px 14px;display:flex;align-items:center;gap:13px;padding-left:14px}
.login input{width:106px;height:20px;border:none;border-radius:3px;font:11px Arimo,sans-serif;padding-left:10px;color:#aaa}
.login button{background:linear-gradient(#4fb0ee,var(--blue-dark));color:#fff;border:2px solid #cfe8f8;border-radius:6px;font:500 13px Ubuntu,sans-serif;padding:2px 6px}
.nav{left:68px;top:107px;width:1014px;height:35px;background:linear-gradient(var(--blue-light),var(--blue-dark));display:flex}
.nav a{color:#fff;font:500 14px Ubuntu,sans-serif;letter-spacing:.4px;text-decoration:none;line-height:35px;border-right:1px solid rgba(255,255,255,.35);white-space:nowrap}
.nav a:last-child{border:none}
.hero{left:84px;top:158px;width:689px;height:300px;border:1px solid #ddd;border-radius:12px;background:#fff;overflow:hidden;box-shadow:0 14px 14px -12px rgba(0,0,0,.25)}
.hero-photo{position:absolute;right:0;top:0;width:420px;height:300px;background:linear-gradient(90deg,#fff 0,#e8e4e1 30%,#d4b9a5 60%,#cfcfd2)}
.checks{position:absolute;left:18px;top:7px;list-style:none;font-size:12px;letter-spacing:.3px;color:#444}
.checks li{height:28px;display:flex;align-items:center;gap:10px}
.price{left:828px;top:142px;width:239px;height:62px;background:var(--char);border-radius:0 0 12px 12px;color:#fff;text-align:center;font-family:Ubuntu,sans-serif}
.price small{display:block;font-size:15px;font-weight:500;margin-top:8px}
.price strong{font-size:25px;font-weight:700}
.price-tab{left:969px;top:204px;width:76px;height:22px;background:linear-gradient(var(--blue-light),var(--blue-dark));border-radius:0 0 8px 8px}
.cta{height:64px;color:#fff;font:700 31px Ubuntu,sans-serif;display:flex;align-items:center;padding-left:26px;border-radius:14px 0 0 14px}
.cta.trial{left:800px;top:274px;width:285px;background:linear-gradient(#3a3a3a,#767676);padding-left:28px}
.cta.plans{left:803px;top:364px;width:282px;background:linear-gradient(var(--blue-dark),var(--blue-light));padding-left:20px}
.fold{width:0;height:0;border-top:10px solid #333;border-right:12px solid transparent}
.testimonials{left:781px;top:466px;width:278px;height:273px;border:1px solid #ddd;border-radius:16px;background:linear-gradient(#fff,#eee);padding:12px 17px 0 22px}
.testimonials h2{font:700 22px Ubuntu,sans-serif;color:var(--blue);margin-left:4px}
.testimonials blockquote{font-size:12px;line-height:18px;letter-spacing:.3px;text-align:justify;color:#555;margin-top:12px}
.testimonials blockquote b{color:#333}
.testimonials cite{display:block;text-align:right;font:normal 12px Arimo,sans-serif;color:var(--blue);margin-top:8px}
.band{left:60px;top:515px;width:670px;height:171px;background:linear-gradient(var(--blue-dark),var(--blue-light));border-radius:0 24px 24px 0}
.band ul{position:absolute;top:16px;list-style:none;color:#fff;font:12px Ubuntu,sans-serif;letter-spacing:.2px}
.band li{height:24px;padding-left:16px;position:relative}
.band li:before{content:"";position:absolute;left:0;top:4px;border-left:5px solid #fff;border-top:4px solid transparent;border-bottom:4px solid transparent}
.band-tip{width:0;height:0;border-right:17px solid var(--blue-dark)}
.seal{left:553px;top:522px;width:164px;height:164px;border-radius:50%;background:radial-gradient(#3a3a3a,#1c1c1c)}
.ask{left:104px;top:733px;width:626px;height:259px;border:1px solid #d5d5d5;border-radius:14px;background:linear-gradient(#f4f4f4,#e8e8e8)}
.ask h2{font:700 22px Ubuntu,sans-serif;color:var(--blue);padding:10px 32px;height:48px;border-bottom:1px solid var(--line)}
.ask label{position:absolute;font:500 12.5px Ubuntu,sans-serif;color:#444}
.field{position:absolute;border:1px solid #d3d3d3;border-radius:12px;background:linear-gradient(#fff,#f0f0f0)}
.send{left:460px;top:944px;width:88px;height:36px;border-radius:18px;border:2px solid #cfe6f7;background:linear-gradient(#4cb0ee,var(--blue-dark));color:#fff;font:700 18px Ubuntu,sans-serif}
.qa-art{left:565px;top:785px;width:155px;height:190px;border-radius:8px;background:linear-gradient(135deg,#d9d9d9,#a8c8ea 55%,#cfcfcf)}
.video{left:787px;top:766px;width:266px;height:227px;border:1px solid #ddd;border-radius:22px;background:linear-gradient(#fff,#ececec)}
.video-photo{left:800px;top:779px;width:240px;height:180px;border-radius:10px;background:linear-gradient(120deg,#cfd6d0,#a1463f 45%,#3b4b6d 70%,#d9dcd6)}
.video-cap{left:811px;top:968px;font:500 11px Ubuntu,sans-serif;color:#333;display:flex;align-items:center;gap:4px}
.dot{width:7px;height:7px;border-radius:50%;background:#e23a1a;display:inline-block}
.footer{left:77px;top:1017px;width:996px;height:149px;background:linear-gradient(#4d4d4d,#1f1f1f);color:#fff}
.footer h2{position:absolute;left:18px;top:10px;font:700 20px Ubuntu,sans-serif}
.phone-art{position:absolute;left:20px;top:46px;width:78px;height:92px;border-radius:8px;background:linear-gradient(135deg,#d8d8d8,#8a8a8a 50%,#3aa84a)}
.address{position:absolute;left:113px;top:42px;font:700 11px/18px Ubuntu,sans-serif;font-style:normal}
.links{position:absolute;top:22px;list-style:none;font:13px Ubuntu,sans-serif}
.links li{height:28px;padding-left:16px;position:relative}
.links li:before{content:"";position:absolute;left:0;top:5px;width:6px;height:6px;border-radius:50%;background:var(--blue-light)}
.follow{position:absolute;left:792px;top:34px;font:700 21px Ubuntu,sans-serif}
.social{position:absolute;top:72px;width:32px;height:32px;border-radius:50%;background:linear-gradient(#eee,#aaa);border:2px solid #fff}
.copy{top:1179px;font:12px Ubuntu,sans-serif;color:#555}
</style>
</head>
<body>
<div class="abs sheet"></div>

<header>
  <div class="abs header"></div>
  <div class="abs brand">Humming Desk</div>
  <div class="abs tagline">Be Confident your phones are covered<span>whatever you are doing</span></div>
  <form class="abs login"><input value="Username"><input value="Password"><button type="button">Login</button></form>
  <nav class="abs nav">
    <a style="width:104px;padding-left:35px">HOME</a><a style="width:199px;padding-left:33px">PHONE ANSWERING</a><a style="width:200px;padding-left:30px">VIRTUAL RECEPTION</a><a style="width:102px;padding-left:34px">FAQ</a><a style="padding-left:35px">ABOUT US</a>
  </nav>
</header>

<section class="abs hero">
  <div class="hero-photo" role="img" aria-label="Photo of a smiling receptionist wearing a headset"></div>
  <ul class="checks">
    <li><svg width="16" height="14"><path d="M1 7l5 5 9-11" stroke="#1b82c9" stroke-width="3" fill="none"/></svg>Properly trained Australian based operators.</li>
    <li><svg width="16" height="14"><path d="M1 7l5 5 9-11" stroke="#1b82c9" stroke-width="3" fill="none"/></svg>Simple to use. No software to download or IT skills needed.</li>
    <li><svg width="16" height="14"><path d="M1 7l5 5 9-11" stroke="#1b82c9" stroke-width="3" fill="none"/></svg>Calls answered professionally in your company name.</li>
    <li><svg width="16" height="14"><path d="M1 7l5 5 9-11" stroke="#1b82c9" stroke-width="3" fill="none"/></svg>Flexible and customisable answering processes.</li>
    <li><svg width="16" height="14"><path d="M1 7l5 5 9-11" stroke="#1b82c9" stroke-width="3" fill="none"/></svg>Calls screened to your rules.</li>
    <li><svg width="16" height="14"><path d="M1 7l5 5 9-11" stroke="#1b82c9" stroke-width="3" fill="none"/></svg>Important people always put through, you control.</li>
    <li><svg width="16" height="14"><path d="M1 7l5 5 9-11" stroke="#1b82c9" stroke-width="3" fill="none"/></svg>Callers introduced before transfer.</li>
    <li><svg width="16" height="14"><path d="M1 7l5 5 9-11" stroke="#1b82c9" stroke-width="3" fill="none"/></svg>Messages sent to email and/or text.</li>
    <li><svg width="16" height="14"><path d="M1 7l5 5 9-11" stroke="#1b82c9" stroke-width="3" fill="none"/></svg>Messages can be sent to multiple people.</li>
    <li><svg width="16" height="14"><path d="M1 7l5 5 9-11" stroke="#1b82c9" stroke-width="3" fill="none"/></svg>Dedicated local numbers Australia wide.</li>
  </ul>
</section>

<aside>
  <div class="abs price"><small>From as little as</small><strong>$4.90 per week</strong></div>
  <div class="abs price-tab"><svg width="76" height="20"><path d="M33 8l5 5 5-5" stroke="#fff" stroke-width="2.5" fill="none"/></svg></div>
  <div class="abs cta trial">Free Trial</div>
  <div class="abs fold" style="left:1073px;top:338px"></div>
  <div class="abs cta plans">Plans &amp; Pricing</div>
  <div class="abs fold" style="left:1073px;top:428px;border-top-color:var(--blue-dark)"></div>

  <section class="abs testimonials">
    <h2>Testimonials</h2>
    <blockquote>“<b>We have used Callwell for over 25 Years. We feel</b> they have given us competitive pricing, dependable service and have been responsive to our needs”<cite>Birch Partners</cite></blockquote>
    <blockquote>“<b>We have used Callwell for over 25 Years. We feel</b> they have given us competitive pricing, dependable service and have been responsive to our needs”<cite>Birch Partners</cite></blockquote>
  </section>

  <div class="abs video"></div>
  <div class="abs video-photo" role="img" aria-label="Photo of two smiling students holding books"></div>
  <svg class="abs" style="left:886px;top:838px" width="70" height="70"><circle cx="35" cy="35" r="32" fill="rgba(0,0,0,.25)" stroke="#eee" stroke-width="3"/><path d="M27 20l21 15-21 15z" fill="#fff"/></svg>
  <div class="abs video-cap"><span class="dot"></span><span class="dot"></span>&nbsp;Watch Latest Testimonial Video</div>
</aside>

<section>
  <div class="abs band-tip" style="left:60px;top:494px;border-top:21px solid transparent"></div>
  <div class="abs band-tip" style="left:60px;top:686px;border-bottom:21px solid transparent"></div>
  <div class="abs band">
    <ul style="left:25px"><li>Phones causing stress?</li><li>Too many voicemails?</li><li>Callers not leaving messages?</li><li>Callers getting busy tone?</li><li>Missing important calls?</li><li>Missing leads or opportunities?</li></ul>
    <ul style="left:256px"><li>Phones causing stress?</li><li>Too many voicemails?</li><li>Callers not leaving messages?</li><li>Callers getting busy tone?</li><li>Missing important calls?</li><li>Missing leads or opportunities?</li></ul>
  </div>
  <div class="abs seal" role="img" aria-label="Refund 100% policy seal"></div>
</section>

<section>
  <form class="abs ask">
    <h2>Ask us anything !</h2>
    <label style="left:11px;top:73px">Name&nbsp;&nbsp;&nbsp;&nbsp;&nbsp;&nbsp;&nbsp;:</label>
    <div class="field" style="left:80px;top:66px;width:139px;height:30px"></div>
    <label style="left:250px;top:73px">Email&nbsp;&nbsp;&nbsp;&nbsp;:</label>
    <div class="field" style="left:309px;top:66px;width:137px;height:30px"></div>
    <label style="left:11px;top:113px">Question :</label>
    <div class="field" style="left:92px;top:108px;width:354px;height:90px"><svg style="position:absolute;right:0;top:0" width="32" height="88"><line x1="1" y1="0" x2="1" y2="88" stroke="#ccc"/><path d="M12 7l4 4 4-4M12 12l4 4 4-4" stroke="#777" stroke-width="1.5" fill="none"/></svg></div>
  </form>
  <button class="abs send" type="button">Send</button>
  <div class="abs qa-art" role="img" aria-label="Illustration of a blue figure leaning on large Q and A letters"></div>
</section>

<footer class="abs footer">
  <h2>Contact Us</h2>
  <div class="phone-art" role="img" aria-label="Illustration of a mobile phone with green signal waves"></div>
  <address class="address">Humming Desk Pty Ltd<br>ABN: 51 302 918 447<br>Unit 9, 42 Wren St<br>Hollowbrook, NSW 2199<br>info@hummingdesk.com.au</address>
  <ul class="links" style="left:370px"><li>Home</li><li>Phone Answering</li><li>Dairy Management</li><li>Plands and Pricing</li></ul>
  <ul class="links" style="left:555px"><li>Home</li><li>Phone Answering</li><li>Dairy Management</li><li>Plands and Pricing</li></ul>
  <div class="follow">Follow us on</div>
  <div class="social" style="left:782px"></div>
  <div class="social" style="left:840px"></div>
  <div class="social" style="left:898px"></div>
</footer>
<div class="abs copy" style="left:85px">Copyright (C) humming desk 1968 - 2012.</div>
<div class="abs copy" style="right:88px">All Rights Reserved</div>
</body>
</html>
```